'Shires at Roundtable'

We are after a flyer to sell a two day conference to sponsors, delegates and other Councils to participate.
The conference aims to be a forum for Northern Territory Councils to get together and discuss ideas, issues and overcome challenges and isolation in collaboration.
The conference will be a inaugural event with the plan to host a annual two day conference each year with a specific theme relevant to all Northern Territory Councils. - Give the Councils a voice.

```html
<!DOCTYPE html>
<html lang="en">
<head>
<meta charset="utf-8">
<title>Shires at Roundtable – Conference Flyer</title>
<link rel="stylesheet" href="https://fonts.googleapis.com/css2?family=Delius&family=Open+Sans:wght@400;600&display=swap">
<style>
  :root {
    --leaf: #8cc63f;
    --sun: #fbb615;
    --sky: #3fa9e0;
    --ink: #1f1f1f;
    --paper: #ffffff;
    --backdrop: #f2f2f2;
    --badge: #2a9fc4;
  }
  * { box-sizing: border-box; margin: 0; padding: 0; }
  html, body {
    width: 1200px; height: 900px; overflow: hidden;
    background: var(--backdrop);
  }
  .flyer {
    position: absolute; left: 300px; top: 25px;
    width: 600px; height: 850px;
    background: var(--paper);
    overflow: hidden;
    font-family: "Open Sans", Arial, sans-serif;
    color: var(--ink);
  }
  .masthead, .footer-band { position: absolute; left: 0; width: 600px; }
  .masthead { top: 0; height: 180px; }
  .footer-band { top: 718px; height: 132px; }

  .event-title {
    position: absolute; left: 232px; top: 40px;
    font-size: 29px; font-weight: 400; color: var(--paper);
    letter-spacing: 0.2px;
  }
  .event-date {
    position: absolute; right: 60px; top: 80px;
    font-size: 16px; color: var(--paper);
  }

  .brand {
    position: absolute; left: 58px; top: 40px;
    width: 140px; height: 140px; border-radius: 50%;
    background: var(--badge);
    display: flex; align-items: center; justify-content: center;
    text-align: center;
  }
  .brand-name {
    font-family: "Open Sans", Arial, sans-serif;
    font-weight: 600; font-size: 17px; line-height: 21px;
    color: var(--paper);
  }

  .content {
    position: absolute; left: 43px; top: 222px; width: 520px;
  }
  .content h2 {
    font-family: "Delius", "Comic Sans MS", cursive;
    font-weight: 400; font-size: 16px; line-height: 22px;
    color: var(--leaf);
    margin-top: 12px; margin-bottom: 3px;
  }
  .content h2:first-child { margin-top: 0; }
  .content p, .content li {
    font-size: 10.5px; line-height: 17.8px;
  }
  .topics { list-style: none; margin: 2px 0 1px; }
  .topics li { position: relative; padding-left: 22px; margin: 3px 0; }
  .topics li::before {
    content: ""; position: absolute; left: 4px; top: 7px;
    width: 4px; height: 4px; border-radius: 50%;
    background: var(--leaf);
  }

  .site-url {
    position: absolute; left: 43px; top: 786px;
    font-size: 20px; color: var(--paper); letter-spacing: 0.3px;
  }
</style>
</head>
<body>
  <main class="flyer">
    <svg class="masthead" viewBox="0 0 600 180" aria-hidden="true">
      <path d="M0 0 H600 V128 C470 112 360 100 240 118 C150 130 70 138 0 132 Z" fill="var(--leaf)"/>
      <path d="M0 132 C70 138 150 130 240 118 C360 100 470 112 600 128 V142 C470 124 360 114 240 130 C150 142 70 148 0 146 Z" fill="var(--sun)"/>
      <path d="M0 146 C70 148 150 142 240 130 C360 114 470 124 600 142 V148 C470 130 360 121 240 136 C150 147 70 152 0 151 Z" fill="var(--sky)"/>
      <path d="M0 166 C120 150 260 140 380 148 C470 154 540 158 600 154" fill="none" stroke="var(--leaf)" stroke-width="1.2" stroke-dasharray="5 4"/>
    </svg>

    <div class="brand"><span class="brand-name">Wattle Ridge<br>Shire<br>Council</span></div>

    <h1 class="event-title">“Shires at Roundtable”</h1>
    <p class="event-date">13-14 April 2011</p>

    <section class="content">
      <h2>What is it all about?</h2>
      <p>“Shires at Roundtable” is a 2 day conference with the aim of providing a forum for Northern Territory Councils to get together and discuss ideas which will enable us overcome the challenges of isolation.</p>

      <h2>Who is invited?</h2>
      <p>The conference will be for all Northern Territory Councils - giving all Councils a voice.</p>

      <h2>Where and when?</h2>
      <p>Harbourside Convention Centre - 13 and 14 April 2011</p>

      <h2>Is there a program?</h2>
      <p>The program will commence at 8.30am with registration, tea and coffee followed by an array of informative topic points including:</p>
      <ul class="topics">
        <li>Remote Service Delivery</li>
        <li>Outsourcing models for effective business practices</li>
        <li>Identifying and implementing sustainable business practices</li>
      </ul>
      <p>Conference will close at 4.30pm.</p>

      <h2>How do I register?</h2>
      <p>Entry to the conference is free, but places are limited. REGISTER NOW to secure your place by visiting:<br>
      http://www.eventforms.com/s/204816/wattle-ridge-conference<br>
      Registration to the conference closes Friday, 18 March 2011.</p>

      <h2>I need more information!</h2>
      <p>For more information contact Jo Marsden on 08 8900 1234 or email jo.marsden@wattleridge.nt.gov.au</p>
    </section>

    <svg class="footer-band" viewBox="0 0 600 132" aria-hidden="true">
      <path d="M0 10 C120 4 260 2 380 12 C470 20 540 20 600 14" fill="none" stroke="var(--leaf)" stroke-width="1.2" stroke-dasharray="5 4"/>
      <path d="M0 30 C110 18 250 22 360 34 C460 44 540 30 600 18 V132 H0 Z" fill="var(--sky)"/>
      <path d="M0 36 C110 24 250 28 360 40 C460 50 540 36 600 24 V132 H0 Z" fill="var(--sun)"/>
      <path d="M0 48 C110 36 250 40 360 52 C460 62 540 48 600 36 V132 H0 Z" fill="var(--leaf)"/>
    </svg>

    <p class="site-url">www.wattleridge.net.au</p>
  </main>
</body>
</html>
```